Business Card Design

I need a bussiness card that have some picture of a van and lorry.
Updates

Hello I could ask you to print business cards and message to the home address?

Industry/Entity Type

Business

Contact Information for Business Card

K&M Transport LTD
truck and vans fridge
drivers recruitment
k.m-transport@quillmail.example
tel nr 07831452096

```html
<!DOCTYPE html>
<html lang="en">
<head>
<meta charset="utf-8">
<title>K&amp;M Transport LTD – Business Card</title>
<link href="https://fonts.googleapis.com/css2?family=Oswald:wght@300;400&family=Open+Sans:ital,wght@1,700&display=swap" rel="stylesheet">
<style>
  :root {
    --backdrop: #9a9a9a;
    --card-light: #f4f4f4;
    --card-mid: #dedede;
    --ink: #1c1c1c;
    --brand-blue: #1f4fb0;
    --brand-blue-deep: #163c8c;
    --brand-red: #c01a22;
    --photo-light: #d9d9d9;
    --photo-dark: #5a5a5a;
  }
  html, body {
    margin: 0;
    width: 1200px;
    height: 1023px;
    overflow: hidden;
    background: var(--backdrop);
  }
  .canvas {
    position: relative;
    width: 1200px;
    height: 1023px;
  }
  .card {
    position: absolute;
    width: 560px;
    height: 320px;
    border-radius: 26px;
    overflow: hidden;
    box-shadow: 0 6px 18px rgba(0,0,0,0.35);
  }
  .card-back {
    left: 50px;
    top: 110px;
  }
  .truck-photo {
    width: 100%;
    height: 100%;
    background: linear-gradient(160deg, var(--photo-light) 0%, #bdbdbd 45%, var(--photo-dark) 80%, #2e2e2e 100%);
  }
  .card-front {
    left: 590px;
    top: 560px;
    background: linear-gradient(135deg, var(--card-light) 0%, var(--card-mid) 100%);
  }
  .cab-photo {
    position: absolute;
    right: 0;
    top: 110px;
    width: 300px;
    height: 210px;
    background: linear-gradient(135deg, rgba(255,255,255,0) 0%, rgba(190,190,190,0.55) 60%, rgba(160,160,160,0.6) 100%);
  }
  .brand {
    position: absolute;
    left: 210px;
    top: 26px;
    display: flex;
    align-items: center;
    gap: 10px;
  }
  .brand-square {
    width: 30px;
    height: 30px;
    background: var(--brand-blue);
  }
  .brand-name {
    font-family: 'Oswald', sans-serif;
    font-weight: 300;
    font-size: 34px;
    letter-spacing: 1px;
    color: var(--ink);
    text-transform: uppercase;
    line-height: 1;
  }
  .brand-tagline {
    position: absolute;
    left: 250px;
    top: 68px;
    font-family: 'Oswald', sans-serif;
    font-weight: 400;
    font-size: 10px;
    letter-spacing: 1.2px;
    color: var(--ink);
    text-transform: uppercase;
  }
  .contact {
    position: absolute;
    left: 30px;
    top: 100px;
    font-family: 'Oswald', sans-serif;
    font-weight: 300;
    font-size: 16px;
    letter-spacing: 1.4px;
    line-height: 1.35;
    color: var(--ink);
    text-transform: uppercase;
  }
  .swoosh {
    position: absolute;
    left: 0;
    top: 0;
    width: 560px;
    height: 320px;
  }
  .swoosh-text {
    font-family: 'Open Sans', sans-serif;
    font-style: italic;
    font-weight: 700;
    font-size: 11px;
    letter-spacing: 1.5px;
    fill: #ffffff;
  }
</style>
</head>
<body>
<main class="canvas">
  <section class="card card-back">
    <div class="truck-photo" role="img" aria-label="Black and white photograph of a refrigerated articulated truck on a mountain road"></div>
  </section>

  <section class="card card-front">
    <div class="cab-photo" role="img" aria-label="Faint photograph of a white lorry cab"></div>

    <div class="brand">
      <span class="brand-square"></span>
      <span class="brand-name">K&amp;M Transport LTD</span>
    </div>
    <div class="brand-tagline">Truck and vans fridge drivers recruitment</div>

    <div class="contact">
      <div class="contact-email">k.m-transport@quillmail.example</div>
      <div class="contact-phone">07831452096</div>
    </div>

    <svg class="swoosh" viewBox="0 0 560 320" aria-hidden="true">
      <path d="M0,168 Q220,240 470,320 L450,320 Q215,252 0,180 Z" fill="var(--brand-red)"/>
      <path d="M0,180 Q215,252 450,320 L300,320 Q150,282 0,228 Z" fill="var(--brand-blue)"/>
      <path d="M0,218 Q150,274 300,320 L280,320 Q140,284 0,232 Z" fill="var(--brand-blue-deep)" opacity="0.5"/>
      <defs>
        <path id="swoosh-line" d="M8,206 Q200,272 392,320"/>
      </defs>
      <text class="swoosh-text"><textPath href="#swoosh-line" textLength="360" lengthAdjust="spacing">TRUCK AND VANS FRIDGE DRIVERS RECRUITMENT</textPath></text>
    </svg>
  </section>
</main>
</body>
</html>
```